Business cards and stationary for construction company
Brackenfield Construction LLC
RT/KPN/OV Team
Hi, the font is. MicrogrammaDBolExt.
And the Construction llc is Helvetica.
Thanks
Hi contest holder, may I know the font used? Thank you.

```html
<!DOCTYPE html>
<html lang="en">
<head>
<meta charset="utf-8">
<title>Brackenfield Construction LLC — Business Cards</title>
<link rel="stylesheet" href="https://fonts.googleapis.com/css2?family=Arimo:wght@400;700&family=Michroma&display=swap">
<style>
  :root {
    --navy: #2d4573;
    --navy-dark: #243a63;
    --paper: #ffffff;
    --ink: #3a4256;
    --rule: #8d94a5;
    --backdrop: #e9eaed;
  }
  * { margin: 0; padding: 0; box-sizing: border-box; }
  html, body { width: 1200px; height: 988px; overflow: hidden; background: var(--backdrop); }
  .canvas { position: relative; width: 1200px; height: 988px; }
  .card {
    position: absolute; width: 560px; height: 320px;
    box-shadow: 0 6px 18px rgba(0,0,0,.18);
  }
  .card-back { left: 560px; top: 110px; background: var(--navy); color: var(--paper); }
  .card-front { left: 80px; top: 540px; background: var(--paper); color: var(--ink); }

  .brand {
    position: absolute; left: 0; right: 0; display: flex; justify-content: center; align-items: center; gap: 10px;
    font-family: "Michroma", sans-serif; font-size: 28px; letter-spacing: .5px;
  }
  .brand-dot { width: 12px; height: 12px; border-radius: 50%; background: currentColor; }
  .card-back .brand { top: 112px; }
  .card-front .brand { top: 38px; color: var(--navy); }

  .back-web {
    position: absolute; left: 0; right: 0; top: 222px; text-align: center;
    font-family: "Arimo", sans-serif; font-size: 14px; letter-spacing: 4px;
  }

  .company { position: absolute; left: 0; right: 0; top: 96px; text-align: center;
    font-family: "Arimo", sans-serif; font-weight: 700; font-size: 17px; color: var(--navy); }
  .person { position: absolute; left: 0; right: 0; top: 120px; text-align: center;
    font-family: "Arimo", sans-serif; font-size: 13px; }

  .address { position: absolute; right: 300px; top: 198px; text-align: right;
    font-family: "Arimo", sans-serif; font-size: 13px; line-height: 19px; }
  .divider { position: absolute; left: 276px; top: 170px; width: 1px; height: 116px; background: var(--rule); }
  .contacts { position: absolute; left: 290px; top: 176px; list-style: none;
    font-family: "Arimo", sans-serif; font-size: 13px; line-height: 21px; }
  .contacts li { display: flex; align-items: center; gap: 6px; }
  .contacts svg { width: 12px; height: 12px; flex: none; }
</style>
</head>
<body>
<main class="canvas">
  <section class="card card-back" aria-label="Card back">
    <div class="brand"><span class="brand-dot"></span>Brackenfield</div>
    <p class="back-web">www.brackenfield@isp.com</p>
  </section>

  <section class="card card-front" aria-label="Card front">
    <div class="brand"><span class="brand-dot"></span>Brackenfield</div>
    <p class="company">Brackenfield Construction LLC</p>
    <p class="person">Colin R. Marsh</p>

    <address class="address" style="font-style:normal">P.O. Box 219<br>Larkdale, OR 97099</address>
    <div class="divider"></div>
    <ul class="contacts">
      <li><svg viewBox="0 0 12 12"><circle cx="6" cy="6" r="6" fill="#2d4573"/><path d="M4 3.2l1 1.2-.6.8c.4.9 1 1.5 1.9 1.9l.8-.6 1.2 1-.7 1c-2.4-.3-4.2-2.1-4.5-4.5z" fill="#fff"/></svg>503-555-0142</li>
      <li><svg viewBox="0 0 12 12"><circle cx="6" cy="6" r="6" fill="#2d4573"/><path d="M4 3.2l1 1.2-.6.8c.4.9 1 1.5 1.9 1.9l.8-.6 1.2 1-.7 1c-2.4-.3-4.2-2.1-4.5-4.5z" fill="#fff"/></svg>503-555-0187</li>
      <li><svg viewBox="0 0 12 12"><circle cx="6" cy="6" r="6" fill="#2d4573"/><rect x="3" y="4" width="6" height="4" fill="none" stroke="#fff" stroke-width=".9"/><path d="M3 4l3 2.3L9 4" fill="none" stroke="#fff" stroke-width=".9"/></svg>brackenfield@isp.com</li>
      <li><svg viewBox="0 0 12 12"><circle cx="6" cy="6" r="6" fill="#2d4573"/><circle cx="6" cy="6" r="3" fill="none" stroke="#fff" stroke-width=".9"/><path d="M3 6h6M6 3v6" stroke="#fff" stroke-width=".7"/></svg>www.brackenfield@isp.com</li>
    </ul>
  </section>
</main>
</body>
</html>
```